Dune Air & Plus business card

I need an awesome, double-sided business card designed with our new logo. I would like the one side black with the colored logo, and the back side is all yours. I'd like to see horizontal and vertical layouts. Get creative! Thank you.

Target Market(s)

HVAC, Heating and Cooling in Phoenix, AZ

Industry/Entity Type

HVAC

Contact Information for Business Card

We need our new logo on the card. Tom Harker, (623) 555-0142, tom@trydunesair.com, www.trydunesair.com, ROC 514273

```html
<!DOCTYPE html>
<html lang="en">
<head>
<meta charset="utf-8">
<title>Dune Air &amp; Plus — Business Card</title>
<link href="https://fonts.googleapis.com/css2?family=Questrial&display=swap" rel="stylesheet">
<style>
  :root {
    --stage: #e9e6e2;
    --paper: #ffffff;
    --paper-shade: #f1f1f1;
    --ink-blue: #2f86d6;
    --accent-orange: #f0a21e;
    --band-orange: #d8761a;
    --card-black: #111214;
    --card-grey: #3a3b3e;
    --panel-1: #1c1d20;
    --panel-2: #0c0c0e;
  }
  * { box-sizing: border-box; margin: 0; padding: 0; }
  html, body {
    width: 1200px; height: 960px; overflow: hidden;
    background: var(--stage);
    font-family: "Questrial", "Century Gothic", sans-serif;
  }
  .canvas { position: relative; width: 1200px; height: 960px; }

  /* Front: portrait white card */
  .card-front {
    position: absolute; left: 50px; top: 148px;
    width: 380px; height: 665px;
    background: linear-gradient(160deg, var(--paper) 40%, var(--paper-shade));
    box-shadow: 0 14px 30px rgba(0,0,0,.25);
    overflow: hidden;
  }
  .brand-mark {
    position: absolute; top: 70px; left: 0; right: 0;
    display: flex; align-items: center; justify-content: center; gap: 12px;
  }
  .brand-dot { width: 26px; height: 26px; border-radius: 50%; background: var(--ink-blue); }
  .brand-name { font-size: 30px; color: var(--ink-blue); letter-spacing: .5px; }
  .holder-name {
    position: absolute; top: 222px; left: 0; right: 0; text-align: center;
    font-size: 34px; letter-spacing: 4px; color: var(--accent-orange);
  }
  .contact-divider { position: absolute; top: 278px; left: 0; width: 380px; height: 60px; }
  .contact-list {
    position: absolute; top: 356px; left: 0; right: 0; text-align: center;
    list-style: none; color: var(--ink-blue); font-size: 21px; line-height: 1.3;
  }
  .licence-band {
    position: absolute; left: 0; right: 0; bottom: 0; height: 112px;
    background: var(--band-orange);
    display: flex; align-items: center; justify-content: center;
    color: #fff; font-size: 24px; letter-spacing: 1px;
  }

  /* Back: landscape black card */
  .card-back {
    position: absolute; left: 480px; top: 290px;
    width: 665px; height: 380px;
    background: radial-gradient(circle at 45% 40%, var(--card-grey), var(--card-black) 65%);
    box-shadow: 0 14px 30px rgba(0,0,0,.3);
    overflow: hidden;
  }
  .back-panels { position: absolute; right: -40px; top: 20px; width: 420px; height: 380px; }
  .back-brand {
    position: absolute; right: 52px; top: 168px; width: 250px;
    display: flex; align-items: center; justify-content: center; gap: 10px;
  }
  .back-brand .brand-dot { width: 20px; height: 20px; background: var(--accent-orange); }
  .back-brand .brand-name { font-size: 25px; color: var(--accent-orange); }
</style>
</head>
<body>
<main class="canvas">

  <section class="card-front" aria-label="Card front">
    <div class="brand-mark">
      <span class="brand-dot"></span>
      <span class="brand-name">Dune Air &amp; Plus</span>
    </div>

    <h1 class="holder-name">TOM HARKER</h1>

    <svg class="contact-divider" viewBox="0 0 380 60" aria-hidden="true">
      <line x1="0" y1="30" x2="112" y2="30" stroke="var(--ink-blue)" stroke-width="1.5"/>
      <line x1="268" y1="30" x2="380" y2="30" stroke="var(--ink-blue)" stroke-width="1.5"/>
      <path d="M128 6 H252 L268 30 L252 54 H128 L112 30 Z" fill="none" stroke="var(--ink-blue)" stroke-width="1.5" stroke-linejoin="round"/>
      <!-- phone -->
      <rect x="148" y="20" width="13" height="20" rx="2" fill="none" stroke="var(--accent-orange)" stroke-width="2"/>
      <!-- mail -->
      <rect x="180" y="22" width="22" height="16" fill="var(--accent-orange)"/>
      <path d="M180 22 L191 31 L202 22" fill="none" stroke="#fff" stroke-width="1.5"/>
      <!-- globe -->
      <circle cx="230" cy="30" r="10" fill="var(--accent-orange)"/>
      <path d="M220 30 H240 M230 20 V40 M223 24 H237 M223 36 H237" stroke="#fff" stroke-width="1.2" fill="none"/>
    </svg>

    <ul class="contact-list">
      <li>(623) 555-0142</li>
      <li>tom@trydunesair.com</li>
      <li>www.trydunesair.com</li>
    </ul>

    <footer class="licence-band">ROC 514273</footer>
  </section>

  <section class="card-back" aria-label="Card back">
    <svg class="back-panels" viewBox="0 0 420 380" aria-hidden="true">
      <path d="M90 30 H330 Q360 30 375 56 L410 120 Q420 140 410 160 L375 224 Q360 250 330 250 H90 Q60 250 45 224 L10 160 Q0 140 10 120 L45 56 Q60 30 90 30 Z"
            transform="translate(0,40) scale(1,1.1)" fill="var(--panel-1)"/>
      <path d="M110 60 H310 Q335 60 347 82 L376 132 Q384 148 376 164 L347 214 Q335 236 310 236 H110 Q85 236 73 214 L44 164 Q36 148 44 132 L73 82 Q85 60 110 60 Z"
            transform="translate(0,24) scale(1,1.1)" fill="var(--panel-2)"/>
    </svg>
    <div class="back-brand">
      <span class="brand-dot"></span>
      <span class="brand-name">Dune Air &amp; Plus</span>
    </div>
  </section>

</main>
</body>
</html>
```